Hearth Bloom Workshop needs a brochure designed.

Larkfen Studio is an interior design firm based in Sydney. We will be running Hearth Bloom Workshops
for all people interested in learning how to decorate
their home. It is important to show modern interior images to attract and excite their creative juices!
Colours we would like is a dark charcoal background
with Chartreuse trim for our logo and for the brochure.
We have attached some of our ideas on wording.
Our images can be replaced or changed to suit your
design.
The final design should be very stylish and to instill a desire to attend our workshops!

Target Market(s)

Mainly female adults in Sydney, aged approx. 25 to 60, who are interested in
interior decorating their homes.

Industry/Entity Type

Learning

Colors
5c5c5c
acd036

Requirements
Must have
• Must show good visual images to catch attention.
Nice to have
• Page layout i.e. to uploaded document, but open to any designs that work better.

```html
<!DOCTYPE html>
<html lang="en">
<head>
<meta charset="utf-8">
<title>Hearth Bloom Workshop – Larkfen Studio</title>
<link href="https://fonts.googleapis.com/css2?family=Lobster&family=Cabin:ital,wght@0,500;1,600;1,700&display=swap" rel="stylesheet">
<style>
  :root {
    --charcoal: #5c5c5c;
    --chartreuse: #acd036;
    --olive: #7ba03a;
    --white: #ffffff;
    --ink: #4a4a4a;
  }
  * { margin: 0; padding: 0; box-sizing: border-box; }
  html, body { width: 1200px; height: 898px; overflow: hidden; background: var(--white); }
  .brochure { position: relative; width: 1200px; height: 898px; font-family: "Cabin", sans-serif; }
  .panel { position: absolute; top: 0; height: 898px; overflow: hidden; }
  .panel--learn { left: 0; width: 400px; background: var(--white); }
  .panel--details { left: 402px; width: 400px; background: var(--white); }
  .panel--gallery { left: 802px; width: 398px; background: var(--white); }
  .divider { position: absolute; top: 0; left: 400px; width: 2px; height: 898px; background: #e6e6e6; }

  .shape { position: absolute; left: 0; top: 0; }
  .learn-title {
    position: absolute; left: 17px; top: 10px;
    font-family: "Lobster", cursive; font-size: 40px; color: var(--white); font-weight: 400;
  }
  .learn-list { position: absolute; left: 22px; top: 104px; width: 340px; list-style: none; }
  .learn-list li {
    font-style: italic; font-weight: 600; font-size: 16px; line-height: 20px;
    color: var(--ink); margin-bottom: 20px;
  }
  .learn-list li::before { content: "• "; }
  .learn-note {
    position: absolute; left: 30px; top: 496px; width: 340px; text-align: center;
    color: var(--white); font-style: italic; font-weight: 600; font-size: 17.5px; line-height: 24px;
  }

  .photo { position: absolute; }
  .photo--bedroom-soft { left: 0; top: 634px; width: 400px; height: 264px;
    background: linear-gradient(160deg, #e7e2da 0%, #cfc4b4 45%, #8e8577 100%); }
  .photo--lounge-plum { left: 0; top: 36px; width: 396px; height: 296px;
    background: linear-gradient(120deg, #e9e6e2 0%, #6e4a5a 40%, #b07a4a 75%, #ece8e2 100%); }
  .photo--bedroom-warm { left: 0; top: 40px; width: 398px; height: 332px;
    background: linear-gradient(150deg, #8c7860 0%, #c9a97a 35%, #6b5540 70%, #3c2f24 100%); }
  .photo--open-living { left: 0; top: 372px; width: 398px; height: 262px;
    background: linear-gradient(170deg, #efece6 0%, #ddd6cb 45%, #b6773e 80%, #8f5a2d 100%); }
  .photo--lounge-rugs { left: 0; top: 636px; width: 398px; height: 219px;
    background: linear-gradient(170deg, #f0ece5 0%, #d8cfc2 45%, #a8683a 85%, #7e4c27 100%); }

  .band { position: absolute; left: 0; width: 100%; }

  .details-facts {
    position: absolute; left: 0; top: 382px; width: 400px; text-align: center;
    color: var(--white); font-style: italic; font-weight: 700; font-size: 19px; line-height: 26px;
  }
  .details-facts p { margin-bottom: 26px; }
  .details-facts .facts-limit { width: 340px; margin: 0 auto 26px; }
  .details-contact {
    position: absolute; left: 23px; top: 745px; width: 360px;
    color: var(--white); font-weight: 500; font-size: 17.5px; line-height: 24px; letter-spacing: 0.2px;
  }
</style>
</head>
<body>
<main class="brochure">

  <section class="panel panel--learn">
    <svg class="shape" width="400" height="634" viewBox="0 0 400 634" aria-hidden="true">
      <polygon points="0,0 400,0 400,68 0,90" fill="var(--chartreuse)"/>
      <polygon points="0,464 400,484 400,608 0,608" fill="var(--charcoal)"/>
      <rect x="0" y="608" width="400" height="12" fill="var(--chartreuse)"/>
      <rect x="0" y="620" width="400" height="4" fill="var(--olive)"/>
    </svg>
    <h1 class="learn-title">You will learn</h1>
    <ul class="learn-list">
      <li>Where and how to use colour, shape, form, and different textures to create a balanced and harmonious environment.</li>
      <li>Current styles and what inspires you.</li>
      <li>Space planning and furniture placement for your room to give a balanced and spacious feel.</li>
      <li>Where to start!</li>
      <li>How to bring it all together with the finishing touches.</li>
      <li>Why Concept plans and mood boards are important.</li>
    </ul>
    <p class="learn-note">You will also enjoy making your very own mood board which will give you insight and inspire you to commence your project with confidence.</p>
    <div class="photo photo--bedroom-soft" role="img" aria-label="Bright bedroom with teal cushions, lamps and a balcony view"></div>
  </section>

  <div class="divider"></div>

  <section class="panel panel--details">
    <div class="band" style="top:0;height:20px;background:var(--olive)"></div>
    <div class="photo photo--lounge-plum" role="img" aria-label="Open-plan lounge with plum feature wall, grey sofa and timber floor"></div>
    <div class="band" style="top:346px;height:16px;background:var(--chartreuse)"></div>
    <div class="band" style="top:362px;height:260px;background:var(--olive)"></div>
    <div class="details-facts">
      <p>All Materials and Lunch are provided.</p>
      <p>Bookings are essential.</p>
      <p class="facts-limit">Numbers are limited to 10 per work-shop</p>
      <p>Cost:&nbsp; $240 (including lunch)</p>
    </div>
    <div class="band" style="top:622px;height:22px;background:var(--chartreuse)"></div>
    <div class="band" style="top:644px;height:20px;background:var(--olive)"></div>
    <div class="band" style="top:664px;height:14px;background:var(--chartreuse)"></div>
    <div class="band" style="top:693px;height:29px;background:var(--charcoal)"></div>
    <div class="band" style="top:732px;height:166px;background:var(--olive)"></div>
    <p class="details-contact">For more information, dates, times and venues of upcoming workshops, please call Maren on Mob 0400518236, or&nbsp; visit our Website www.larkfenstudio.com.au</p>
  </section>

  <section class="panel panel--gallery">
    <div class="photo photo--bedroom-warm" role="img" aria-label="Warm bedroom with stone feature wall, fur throw and bedside lamps"></div>
    <svg class="shape" width="398" height="180" viewBox="0 0 398 180" aria-hidden="true">
      <polygon points="0,0 398,0 398,0 0,62" fill="var(--charcoal)"/>
      <polygon points="0,62 398,0 398,12 0,78" fill="var(--white)"/>
      <polygon points="0,78 398,12 398,40 0,110" fill="var(--chartreuse)"/>
      <polygon points="0,110 398,40 398,48 0,124" fill="var(--white)"/>
      <polygon points="0,124 398,48 398,60 0,156" fill="var(--chartreuse)"/>
      <polygon points="0,156 398,60 398,66 0,168" fill="var(--white)"/>
    </svg>
    <div class="photo photo--open-living" role="img" aria-label="Open living and dining room with patterned chairs and garden view"></div>
    <div class="photo photo--lounge-rugs" role="img" aria-label="Lounge with red-accent armchairs, glass coffee table and shag rug"></div>
    <svg class="shape" style="top:842px" width="398" height="56" viewBox="0 0 398 56" aria-hidden="true">
      <polygon points="0,14 398,0 398,56 0,56" fill="var(--white)"/>
      <polygon points="0,44 398,26 398,56 0,56" fill="var(--chartreuse)"/>
    </svg>
  </section>

</main>
</body>
</html>
```